Women's Clothing / Pip & Tansy's
I'd prefer to have the logo centered at the top of the letterhead and have the address, etc. listed on the bottom. Also, I'm not fond of the little icons that indicate address, phone, email, web. Maybe an envelope with just the logo on the front and the return address on the flap? I think they all look really busy with the big logo in the corner and the address on the bottom. It's something I won't use often, so simple is good.
I really like the front of the business card in #4 and the back of the card in purple. More feedback later on the rest. Thanks for all of the options so far!
Cute design, thanks! What would it look like if the back was purple and the logo was white?

```html
<!DOCTYPE html>
<html lang="en">
<head>
<meta charset="utf-8">
<title>Pip &amp; Tansy's – Business Card</title>
<link rel="stylesheet" href="https://fonts.googleapis.com/css2?family=Open+Sans:wght@400;600;700&display=swap">
<style>
  :root {
    --backdrop: #2e2e2e;
    --card: #ffffff;
    --plum: #9b3d84;
    --plum-dark: #7e2f6b;
    --tangerine: #f0923a;
    --ink: #3a3a3a;
    --rule: #c9c9c9;
  }
  * { margin: 0; padding: 0; box-sizing: border-box; }
  html, body {
    width: 1200px; height: 780px; overflow: hidden;
    background: var(--backdrop);
    font-family: "Open Sans", Arial, sans-serif;
  }
  .business-card {
    position: absolute; left: 100px; top: 100px;
    width: 1000px; height: 580px;
    background: var(--card);
    border-radius: 36px;
    overflow: hidden;
    box-shadow: 0 14px 40px rgba(0,0,0,.45);
  }
  .accent-line {
    position: absolute; left: 0; right: 0; height: 3px;
    background: var(--tangerine);
  }
  .accent-line--top { top: 78px; }
  .accent-line--bottom { top: 202px; }
  .name-band {
    position: absolute; left: 0; right: 0; top: 88px; height: 104px;
    background: var(--plum);
  }
  .holder {
    position: absolute; right: 48px; top: 104px;
    text-align: right; color: #fff;
  }
  .holder__name { font-size: 30px; font-weight: 700; line-height: 1.2; }
  .holder__title { font-size: 20px; font-weight: 600; line-height: 1.4; }
  .brand-dot {
    position: absolute; left: 300px; top: 68px;
    width: 144px; height: 144px; border-radius: 50%;
    background: var(--plum-dark);
    border: 8px solid var(--card);
  }
  .brand-name {
    position: absolute; left: 120px; width: 500px; top: 232px;
    text-align: center;
    font-size: 60px; font-weight: 600; color: var(--plum);
    line-height: 1.1;
  }
  .brand-tagline {
    position: absolute; left: 120px; width: 500px; top: 306px;
    text-align: center;
    font-size: 15px; letter-spacing: 5px; color: var(--tangerine);
    text-transform: uppercase;
  }
  .address {
    position: absolute; right: 530px; top: 420px;
    text-align: right; font-size: 22px; color: var(--ink); line-height: 1.5;
  }
  .contact-divider {
    position: absolute; left: 492px; top: 398px;
    width: 2px; height: 118px; background: var(--rule);
  }
  .contact-list {
    position: absolute; left: 512px; top: 396px;
    list-style: none;
  }
  .contact-list li {
    display: flex; align-items: center; gap: 12px;
    height: 40px; font-size: 21px; color: var(--ink);
  }
  .contact-list svg { width: 24px; height: 24px; flex: none; }
</style>
</head>
<body>
  <article class="business-card">
    <div class="accent-line accent-line--top"></div>
    <div class="name-band"></div>
    <div class="accent-line accent-line--bottom"></div>

    <div class="brand-dot"></div>

    <div class="holder">
      <p class="holder__name">Marla Quenby</p>
      <p class="holder__title">Proprietor</p>
    </div>

    <p class="brand-name">Pip &amp; Tansy's</p>
    <p class="brand-tagline">Apparel • Accessories • Gifts</p>

    <address class="address" style="font-style:normal">
      742 Alder Lane<br>
      Brookvale, ST 00412
    </address>

    <div class="contact-divider"></div>

    <ul class="contact-list">
      <li>
        <svg viewBox="0 0 24 24" aria-hidden="true"><path fill="#9b3d84" d="M6.6 10.8a15 15 0 0 0 6.6 6.6l2.2-2.2a1 1 0 0 1 1-.25 11.4 11.4 0 0 0 3.6.57 1 1 0 0 1 1 1V20a1 1 0 0 1-1 1A17 17 0 0 1 3 4a1 1 0 0 1 1-1h3.5a1 1 0 0 1 1 1c0 1.25.2 2.45.57 3.57a1 1 0 0 1-.25 1z"/></svg>
        555-014-2278
      </li>
      <li>
        <svg viewBox="0 0 24 24" aria-hidden="true"><circle cx="12" cy="12" r="4" fill="none" stroke="#9b3d84" stroke-width="2.4"/><path d="M16 8v5.5a2.5 2.5 0 0 0 5 0V12a9 9 0 1 0-3.5 7.1" fill="none" stroke="#9b3d84" stroke-width="2.4" stroke-linecap="round"/></svg>
        corbelwrenx@pipandtansys.com
      </li>
      <li>
        <svg viewBox="0 0 24 24" aria-hidden="true"><g fill="none" stroke="#9b3d84" stroke-width="2"><circle cx="12" cy="12" r="9"/><ellipse cx="12" cy="12" rx="4" ry="9"/><path d="M3 12h18"/></g></svg>
        www.pipandtansys.com
      </li>
    </ul>
  </article>
</body>
</html>
```